Business card design for new, innovative company - BluePlinth

We are a new company looking for a business card design that is fun, different and quirky. Must use corporate colour green - CMYK C:55, M:0, Y:100, K:0, and corporate colour grey - C:0, M:0, Y: 0, K:70.

We have developed the first real time data application, in which people are able to profile the data of their existing customers in order to pull out more good fit clients to direct their marketing activities at.

Industry/Entity Type

Marketing

Requirements
Must have
• Logo, name, title, telephone number, fax number, email, website, address

```html
<!DOCTYPE html>
<html lang="en">
<head>
<meta charset="utf-8">
<title>BluePlinth Business Card</title>
<link rel="stylesheet" href="https://fonts.googleapis.com/css2?family=Source+Sans+3:wght@400;600&display=swap">
<style>
  :root {
    --brand-green: #7ac143;
    --brand-grey: #6a6b6e;
    --line-grey: #66636e;
    --name-cream: #f2f0c6;
    --text-white: #ffffff;
    --page-bg: #e6e6e4;
  }
  html, body {
    margin: 0;
    width: 1200px;
    height: 900px;
    overflow: hidden;
    background: var(--page-bg);
  }
  .canvas {
    position: relative;
    width: 1200px;
    height: 900px;
  }
  .card {
    position: absolute;
    top: 300px;
    width: 500px;
    height: 300px;
    box-shadow: 0 6px 18px rgba(0,0,0,0.25);
  }
  .card--front { left: 70px; }
  .card--back { left: 630px; }
  .card svg { display: block; }
  .brand-name {
    font-family: "Source Sans 3", sans-serif;
    font-weight: 600;
    fill: var(--text-white);
  }
  .holder-name {
    font-family: "Source Sans 3", sans-serif;
    font-weight: 600;
    font-size: 23px;
    fill: var(--name-cream);
  }
  .contact-line {
    font-family: "Source Sans 3", sans-serif;
    font-weight: 400;
    font-size: 9.5px;
    fill: var(--text-white);
  }
  .web-line {
    font-family: "Source Sans 3", sans-serif;
    font-weight: 400;
    font-size: 9px;
    fill: var(--text-white);
  }
</style>
</head>
<body>
<main class="canvas">

  <section class="card card--front" aria-label="Business card front">
    <svg width="500" height="300" viewBox="0 0 500 300">
      <rect class="card-pattern" role="img" aria-label="Green background with a repeating wave pattern" width="500" height="300" fill="var(--brand-green)"/>
      <path class="track-outline" d="M500 40 H130 A110 110 0 0 0 130 260 H500" fill="none" stroke="var(--line-grey)" stroke-width="6"/>
      <path class="track-panel" d="M500 64 H128 A86 86 0 0 0 128 236 H500 Z" fill="var(--brand-grey)"/>
      <text class="brand-name" x="62" y="163" font-size="40">BluePlinth</text>
      <text class="holder-name" x="283" y="108">Carys Whitfield</text>
      <g class="contact-details">
        <text class="contact-line" x="283" y="136">22c Alder Lane, Ely, Cambridgeshire,</text>
        <text class="contact-line" x="283" y="148">CB7 4QT</text>
        <text class="contact-line" x="283" y="166">M: 07700 900482</text>
        <text class="contact-line" x="283" y="181">T: 01353 960214</text>
        <text class="contact-line" x="283" y="196">E: carys.whitfield@blueplinth.com</text>
        <text class="contact-line" x="283" y="211">W: www.blueplinth.com</text>
      </g>
    </svg>
  </section>

  <section class="card card--back" aria-label="Business card back">
    <svg width="500" height="300" viewBox="0 0 500 300">
      <rect class="card-pattern" role="img" aria-label="Grey background with a repeating green wave pattern" width="500" height="300" fill="var(--brand-grey)"/>
      <circle class="emblem-ring" cx="250" cy="145" r="116" fill="none" stroke="var(--brand-green)" stroke-width="8"/>
      <circle class="emblem-disc" cx="250" cy="145" r="98" fill="var(--brand-green)"/>
      <text class="brand-name" x="250" y="155" font-size="32" text-anchor="middle">BluePlinth</text>
      <text class="web-line" x="250" y="200" text-anchor="middle">www.blueplinth.com</text>
    </svg>
  </section>

</main>
</body>
</html>
```